We require a banner design for a 53' x 10' trailer for a future development to be displayed on the side of the highway. The development name is 712 35 Commerce Park, logo is attached. This is an industrial future development. Please also include the RLW Group logo and MERO Development logos as well.

Industry/Entity Type

Real Estate / Construction / Developer / Industrial Future Development

Requirements
Must have
• Logos provided

```html
<!DOCTYPE html>
<html lang="en">
<head>
<meta charset="utf-8">
<title>712 35 Commerce Park – Future Development Site Trailer Banner</title>
<link rel="stylesheet" href="https://fonts.googleapis.com/css2?family=Archivo+Black&family=Montserrat:wght@400;700;800&display=swap">
<style>
  :root{
    --page-bg:#d9d8dc;
    --paper:#f6f6f9;
    --ink:#241b27;
    --violet:#3a2fd6;
    --violet-deep:#10097a;
    --violet-mid:#2a1fc2;
    --accent-red:#e8203a;
    --frame:#6b4b57;
    --divider:#d2d0da;
    --white:#ffffff;
  }
  *{margin:0;padding:0;box-sizing:border-box}
  html,body{width:1200px;height:1200px;overflow:hidden;background:var(--page-bg)}
  .banner{
    position:absolute;left:20px;top:490px;width:1160px;height:219px;
    background:var(--paper);overflow:hidden;
    box-shadow:0 8px 24px rgba(0,0,0,.18);
  }
  .banner__art{position:absolute;inset:0;width:1160px;height:219px}

  .brand{position:absolute;left:34px;top:20px;color:var(--ink);font-family:"Montserrat",sans-serif}
  .brand__number{display:flex;flex-direction:column;align-items:flex-end;width:114px;
    font-weight:800;font-size:44px;line-height:.84;letter-spacing:-1px}
  .brand__row{display:flex;align-items:center;gap:7px}
  .brand__square{width:26px;height:26px;border:3px solid var(--frame)}
  .brand__name{margin-top:9px;font-weight:400;font-size:11px;letter-spacing:1.8px}

  .partners{position:absolute;left:34px;top:164px;display:flex;align-items:center;
    font-family:"Montserrat",sans-serif;color:var(--ink)}
  .partner{display:flex;align-items:center;gap:6px}
  .partner__dot{width:10px;height:10px;border-radius:50%;background:var(--accent-red)}
  .partner__name{font-weight:700;font-size:15px;letter-spacing:.4px}
  .partners__divider{width:1px;height:30px;background:var(--divider);margin:0 11px}
  .partner--mero{flex-direction:column;align-items:flex-start;gap:1px}
  .partner__sub{font-size:6px;letter-spacing:1.6px}

  .headline{
    position:absolute;left:320px;top:22px;width:560px;
    display:flex;flex-direction:column;align-items:center;
    font-family:"Archivo Black",sans-serif;color:var(--white);
    transform:rotate(-3deg);
    text-shadow:1px 1px 0 #9a93f0,2px 3px 0 #5a4fe6,3px 4px 0 #3a2fd6,4px 6px 8px rgba(10,5,80,.5);
  }
  .headline__park{font-size:18px;line-height:1.2}
  .headline__future{font-size:86px;line-height:.98;letter-spacing:-1px;
    text-shadow:2px 2px 0 #9a93f0,3px 5px 0 #5a4fe6,5px 8px 0 #3a2fd6,7px 11px 12px rgba(10,5,80,.55)}
  .headline__site{font-size:30px;line-height:1.15}
  .headline__tagline{font-size:18px;line-height:1.2}
</style>
</head>
<body>
<main class="banner">
  <svg class="banner__art" viewBox="0 0 1160 219">
    <defs>
      <linearGradient id="band-silver" x1="0" y1="0" x2="0" y2="1">
        <stop offset="0" stop-color="#b8b0cc"/>
        <stop offset="1" stop-color="#eeeef4"/>
      </linearGradient>
      <linearGradient id="field-violet" x1="0" y1="0" x2="0" y2="1">
        <stop offset="0" stop-color="#8a84e6"/>
        <stop offset=".45" stop-color="var(--violet-mid)"/>
        <stop offset="1" stop-color="var(--violet-deep)"/>
      </linearGradient>
      <linearGradient id="skyline-tone" x1="0" y1="0" x2="1" y2="1">
        <stop offset="0" stop-color="#e2e0f6" stop-opacity=".85"/>
        <stop offset=".55" stop-color="#7f86d8" stop-opacity=".65"/>
        <stop offset="1" stop-color="#3b36c8" stop-opacity=".5"/>
      </linearGradient>
      <linearGradient id="venue-tone" x1="0" y1="0" x2="1" y2="0">
        <stop offset="0" stop-color="#4fa13a"/>
        <stop offset=".45" stop-color="#5c7b8f"/>
        <stop offset="1" stop-color="#aab8cc"/>
      </linearGradient>
    </defs>
    <polygon class="band-silver" points="236,219 306,0 326,0 256,219" fill="url(#band-silver)"/>
    <polygon class="field-violet" points="266,219 336,0 1160,0 1160,219" fill="url(#field-violet)"/>
    <polygon class="photo-skyline" role="img"
      aria-label="Photo of glass office towers, trees and a roadside verge under a cloudy sky"
      points="336,0 1160,0 1160,112 301,112" fill="url(#skyline-tone)"/>
    <polygon class="photo-venue" role="img"
      aria-label="Photo of a domed convention building with twin towers, green trees and a street"
      points="890,219 905,178 960,158 1010,130 1060,124 1085,92 1120,94 1160,100 1160,219"
      fill="url(#venue-tone)"/>
  </svg>

  <header class="brand" aria-label="712 35 Commerce Park">
    <div class="brand__number">
      <span>712</span>
      <span class="brand__row"><span class="brand__square"></span>35</span>
    </div>
    <div class="brand__name">COMMERCE PARK</div>
  </header>

  <h1 class="headline">
    <span class="headline__park">712 35 COMMERCE PARK</span>
    <span class="headline__future">FUTURE</span>
    <span class="headline__site">DEVELOPMENT SITE</span>
    <span class="headline__tagline">A NEW ERA IN BUSINESS</span>
  </h1>

  <footer class="partners">
    <div class="partner partner--rlw">
      <span class="partner__dot"></span>
      <span class="partner__name">RLW</span>
    </div>
    <span class="partners__divider"></span>
    <div class="partner partner--mero">
      <span class="partner__name">MERO</span>
      <span class="partner__sub">DEVELOPMENT</span>
    </div>
  </footer>
</main>
</body>
</html>
```